Redesign criminal justice consulting website

We run a small professional services firm that does research, evaluation, consulting, and training on criminal justice issues. We need to redesign our website (www.brvolquest.com). The existing site is something we made ourselves. It is unprofessional and does not do a good job of communicating what we do or who we are.

We would like the new site to provide a basic overview of what we do. Moreover, we would like it to communicate several themes that represent who we are:

* global

* innovative

* analytical

* practical

We view the principal design challenge as figuring out a subtle, interesting, and graphically appealing way to communicate these themes.

Target Market(s)

Our primary customers are governments, research firms, criminal justice agencies, and schools. The people who we want to find our site are seeking research, evaluation, training, or consulting services related to crime, criminal justice, or policing.

Industry/Entity Type

Consulting

Number of Pages Required

2 pages

Requirements
Must have
• 1. We would like the site to use our logo. It is attached (please use the maroon 4-color version with the company name but without the slogan). The site should also use the colors present in our logo. It may use other colors as well, as long as these colors coordinate with the logo colors.

• 2. For main pages or buttons, we need the following:
• *Home
• *About BVQ
• *Services
• *E-Training
• *Resources
• *Contact BVQ

• 3. We like simple, crisp, subtle designs over "busier," cluttered, or very complex designs.

• 4. We'd like to receive, at a minimum, the home page and a sample inner page.
Nice to have
• We need some help in thinking through what regions or sections should exist on the home page. We are thinking about having a window on there where we can make announcements about recent developments like new reports, new e-training videos, new photographs, etc... We are open to suggestions here.
Should not have
• 1. Gimmicky or overused clipart.
• 2. Cliched images associated with criminal justice, including magnifying glasses, scales of justice, etc... Our logo makes a subtle nod to criminal justice through the use of a fingerprint as the dot on the "J" in the company initials. That''s sufficient for our purposes. Concentrate instead on the themes listed above.
• 3. Major use of colors that don't match our logo, like blue.

```html
<!DOCTYPE html>
<html lang="en">
<head>
<meta charset="utf-8">
<title>BVQ – Home and About</title>
<link rel="stylesheet" href="https://fonts.googleapis.com/css2?family=Arimo:wght@400;700&display=swap">
<style>
  :root {
    --ink: #000000;
    --maroon: #a3290b;
    --maroon-dark: #7e220b;
    --paper: #ffffff;
    --page-bg: #f0efed;
    --panel: #f6f6f6;
    --footer: #e9e8e6;
    --divider: #b7b7b7;
    --body-text: #6e6e6e;
    --heading-text: #1a1a1a;
    --muted: #8a8a8a;
    --hero-dark: #4f4f4b;
    --hero-light: #9b9a93;
  }
  * { box-sizing: border-box; margin: 0; padding: 0; }
  html, body { width: 1200px; height: 2600px; overflow: hidden; }
  body {
    position: relative;
    background: var(--page-bg);
    font-family: "Arimo", Arial, sans-serif;
    color: var(--body-text);
  }
  .page { position: absolute; left: 0; width: 1200px; }
  .page--home { top: 0; height: 1290px; }
  .page--about { top: 1314px; height: 1286px; }
  .page-divider { position: absolute; left: 0; top: 1290px; width: 1200px; height: 24px; background: var(--divider); }

  .masthead { position: absolute; left: 0; top: 0; width: 1200px; background: var(--ink); }
  .page--home .masthead { height: 614px; }
  .page--about .masthead { height: 250px; }

  .brand {
    position: absolute; left: 32px; top: 26px;
    display: flex; align-items: center; gap: 16px;
    color: var(--paper); font-weight: 700; font-size: 72px; letter-spacing: -2px; line-height: 1;
  }
  .brand__dot { width: 22px; height: 22px; border-radius: 50%; background: var(--paper); }

  .main-nav { position: absolute; left: 0; top: 156px; width: 1200px; height: 40px; }
  .main-nav__item {
    position: absolute; top: 0; height: 40px; width: 160px; margin-left: -80px;
    text-align: center; line-height: 40px;
    color: var(--paper); font-weight: 700; font-size: 13px; letter-spacing: 1px;
    text-transform: uppercase;
  }
  .main-nav__item--active { background: var(--maroon); }
  .nav-rule { position: absolute; left: 0; top: 196px; width: 1200px; height: 8px; background: var(--maroon-dark); }

  /* Home hero */
  .hero { position: absolute; left: 30px; top: 210px; width: 1140px; height: 360px; }
  .hero__photo {
    position: absolute; inset: 0;
    background: linear-gradient(100deg, var(--hero-dark) 0%, #6e6d68 45%, var(--hero-light) 100%);
  }
  .hero__title { position: absolute; left: 50px; top: 100px; color: var(--paper); font-size: 40px; font-weight: 700; }
  .hero__subtitle { position: absolute; left: 50px; top: 158px; color: var(--paper); font-size: 22px; font-weight: 700; }
  .hero__text { position: absolute; left: 50px; top: 198px; width: 510px; color: var(--paper); font-size: 13px; font-weight: 700; line-height: 16px; }
  .slider-bar { position: absolute; left: 0; top: 570px; width: 1200px; height: 44px; }
  .slider-dots { position: absolute; right: 96px; top: 14px; display: flex; gap: 4px; }
  .slider-dots__dot { width: 15px; height: 15px; border: 2px solid var(--paper); }
  .slider-dots__dot--on { background: var(--paper); }

  .home-body { position: absolute; left: 30px; top: 614px; width: 1140px; height: 596px; background: var(--paper); }
  .news { position: absolute; left: 82px; top: 30px; width: 316px; }
  .news__title { font-size: 28px; color: var(--heading-text); font-weight: 400; letter-spacing: -0.5px; }
  .news__title em { font-style: normal; color: var(--maroon); }
  .news__photo { margin-top: 18px; width: 316px; height: 170px; background: linear-gradient(160deg, #e4e2de, #bdbab4); }
  .news__headline { margin-top: 24px; font-size: 17px; font-weight: 700; color: var(--heading-text); }
  .news__text { margin-top: 10px; font-size: 16px; line-height: 19px; }
  .news__links { list-style: none; margin-top: 42px; }
  .news__links li { font-size: 17px; line-height: 30px; font-weight: 700; color: var(--maroon); }
  .news__links li::before { content: "»"; color: var(--muted); font-weight: 400; margin-right: 14px; }

  .feature { position: absolute; left: 414px; top: 16px; width: 712px; height: 570px; background: var(--panel); padding: 34px 40px; }
  .feature__headline { font-size: 17px; font-weight: 700; color: var(--heading-text); margin-bottom: 12px; }
  .feature p { font-size: 16px; line-height: 19px; margin-bottom: 19px; }
  .feature__more { font-size: 17px; font-weight: 700; color: var(--maroon); }

  .site-footer {
    position: absolute; left: 0; width: 1200px; height: 80px;
    background: var(--footer); border-top: 6px solid #dcdbd8;
    text-align: center; line-height: 68px;
    font-size: 12px; letter-spacing: 1px; color: var(--muted); text-transform: uppercase;
  }
  .site-footer strong { color: #6a6a6a; }
  .page--home .site-footer { top: 1210px; }
  .page--about .site-footer { top: 1210px; height: 76px; }

  /* About page */
  .about-body { position: absolute; left: 30px; top: 220px; width: 1140px; height: 990px; background: var(--paper); }
  .section-title { position: absolute; left: 82px; font-size: 27px; font-weight: 400; color: var(--maroon); letter-spacing: -0.5px; }
  .team-photo { position: absolute; left: 82px; top: 102px; width: 390px; height: 262px; background: linear-gradient(120deg, #c9ccd0, #8d8f93 55%, #3c3d40); }
  .intro { position: absolute; left: 502px; top: 100px; width: 590px; }
  .intro__lead { font-size: 17px; font-weight: 700; color: #3e3e3e; line-height: 20px; margin-bottom: 18px; }
  .intro p { font-size: 16px; line-height: 19px; margin-bottom: 19px; }
  .pull-line { position: absolute; left: 82px; top: 390px; font-size: 17px; font-weight: 700; color: #3e3e3e; }
  .article { position: absolute; left: 82px; top: 516px; width: 988px; }
  .article p { font-size: 16px; line-height: 19px; margin-bottom: 20px; text-align: left; }
  .article p + p + p { margin-top: 36px; }
</style>
</head>
<body>

<section class="page page--home">
  <header class="masthead">
    <div class="brand"><span class="brand__dot"></span>BVQ</div>
    <nav class="main-nav">
      <span class="main-nav__item main-nav__item--active" style="left:110px">Home</span>
      <span class="main-nav__item" style="left:300px">About BVQ</span>
      <span class="main-nav__item" style="left:490px">Services</span>
      <span class="main-nav__item" style="left:680px">E-Training</span>
      <span class="main-nav__item" style="left:870px">Resources</span>
      <span class="main-nav__item" style="left:1060px">Contact BVQ</span>
    </nav>
    <div class="nav-rule"></div>
    <div class="hero">
      <div class="hero__photo" role="img" aria-label="Brushed metal puzzle piece on a grey surface"></div>
      <h1 class="hero__title">What we do?</h1>
      <p class="hero__subtitle">This is what we’re asked by many people.</p>
      <p class="hero__text">Our clients know we suscipit nibh nisl vel enim ad duis vero ut in eum dolore magna zzril ut, consequat ex feugiat, quis, nostrud ea, vel.</p>
    </div>
    <div class="slider-bar">
      <div class="slider-dots">
        <span class="slider-dots__dot slider-dots__dot--on"></span>
        <span class="slider-dots__dot"></span>
        <span class="slider-dots__dot"></span>
        <span class="slider-dots__dot"></span>
      </div>
    </div>
  </header>

  <main class="home-body">
    <aside class="news">
      <h2 class="news__title">Whats <em>new!</em></h2>
      <div class="news__photo" role="img" aria-label="Stack of folded newspapers"></div>
      <h3 class="news__headline">Vel vulputate nulla et duis amet.</h3>
      <p class="news__text">Exerci nulla, in ipsum esse in ut, wisi nulla consequat eu wisi eum tincidunt vel nostrud.</p>
      <ul class="news__links">
        <li>Exerci nulla</li>
        <li>In ipsum esse in</li>
        <li>Wisi nulla consequat</li>
        <li>Eu wisi eum</li>
        <li>Tincidunt vel nostrud.</li>
      </ul>
    </aside>
    <article class="feature">
      <h2 class="feature__headline">Vel vulputate nulla et duis amet.</h2>
      <p>Exerci nulla, in ipsum esse in ut, wisi nulla consequat eu wisi eum tincidunt vel nostrud.</p>
      <p>Exerci nulla, in ipsum esse in ut, wisi nulla consequat eu wisi eum suscipit dolent ut nostrud at vulputate vel illum molestie minim minim consequat.</p>
      <p>Augue in laoreet, euismod nostrud iusto vel amet wisi iusto .</p>
      <p>Quis duis feugiat adipiscing ut. Lobortis, lobortis velit erat dolore qui. Blandit sit elit minim blandit ullamcorper.</p>
      <p>Augue in laoreet, euismod nostrud iusto vel amet wisi iusto quis duis feug adipiscing ut. Lobortis, lobortis velit er dolore qui.</p>
      <p>Blandit sit elit minim blandit ullamcorpe.</p>
      <span class="feature__more">read more...</span>
    </article>
  </main>

  <footer class="site-footer"><strong>Copyright</strong> | All rights reserved</footer>
</section>

<div class="page-divider"></div>

<section class="page page--about">
  <header class="masthead">
    <div class="brand"><span class="brand__dot"></span>BVQ</div>
    <nav class="main-nav">
      <span class="main-nav__item" style="left:110px">Home</span>
      <span class="main-nav__item main-nav__item--active" style="left:300px">About BVQ</span>
      <span class="main-nav__item" style="left:490px">Services</span>
      <span class="main-nav__item" style="left:680px">E-Training</span>
      <span class="main-nav__item" style="left:870px">Resources</span>
      <span class="main-nav__item" style="left:1060px">Contact BVQ</span>
    </nav>
    <div class="nav-rule"></div>
  </header>

  <main class="about-body">
    <h1 class="section-title" style="top:52px">About BVQ</h1>
    <div class="team-photo" role="img" aria-label="Group of smiling business colleagues"></div>
    <div class="intro">
      <p class="intro__lead">Consequat in feugiat eros duis amet, te, blandit, odio duis te illum aliquip duis aliquam consequat quis, diam vero.</p>
      <p>Exerci nulla, dolor lorem esse in facilisi, ut nulla consequat eu wisi eum ullamcorper euismod autem quis facilisis vulputate vel vel esse ad minim commodo.</p>
      <p>Autem, feugait enim minim vero commodo accumsan delenit ut illum sed vero, hendrerit ut suscipit velit vel, ullamcorper aliquip ea.</p>
      <p>Qui ea eum duis duis blandit dolor accumsan exerci enim nulla dignissim dolore aliquam nulla nibh et velit dolore aliquip consequat wisi ut.</p>
    </div>
    <p class="pull-line">Ut in luptatum dolore dolor ullamcorper et molestie in laoreet, euismod nostrud.</p>

    <h2 class="section-title" style="top:464px">Vel duis</h2>
    <div class="article">
      <p>Vel duis, tincidunt feugait hendrerit iriure ipsum delenit, iriure, odio lobortis veniam, enim luptatum facilisi nulla volutpat. Elit, qui vel facilisis duis eu veniam duis, facilisi dolor feugiat, aliquip, ad lobortis, nonummy. Adipiscing amet, ut consectetuer nibh nostrud sed commodo esse, lobortis dolore praesent odio dolore, accumsan, iusto quis facilisis. Qui ea eum duis duis blandit dolor accumsan exerci enim nulla dignissim dolore aliquam nulla nibh et velit dolore aliquip consequat wisi ut. Duis autem te suscipit volutpat tation velit praesent eum magna, ipsum elit in consectetuer ut hendrerit exerci zzril. Lorem veniam molestie vero eros enim eu vulputate, ut eros nulla. Autem, feugait enim minim vero commodo accumsan delenit ut illum sed vero, hendrerit ut suscipit velit vel, ullamcorper aliquip ea.</p>
      <p>Praesent laoreet, euismod nostrud et vel sit ut iusto quis augue feugiat adipiscing ut. Lobortis, lobortis vulputate erat laoreet dignissim, qui dolor elit minim blandit tation. Eu at diam augue nostrud ex, tation, wisi, erat luptatum tation adipiscing, in. Consectetuer zzril nisl consequat accumsan tincidunt, feugait suscipit dolore nisl et at. Iusto, nisl nonummy molestie qui vel augue eum iriure vel wisi luptatum, lorem.</p>
      <p>Iusto dignissim dolore aliquam nulla nibh et velit dolore aliquip consequat wisi ut dolore autem te suscipit volutpat tation. Te praesent eum magna, ipsum elit in consectetuer ut hendrerit exerci zzril tation veniam molestie vero eros enim eu vulputate, ut eros nulla. Euismod exerci, feugait enim minim vero commodo accumsan delenit ut illum sed vero, hendrerit ut suscipit velit vel, ullamcorper aliquip ea. In praesent dolore veniam in odio duis, tincidunt feugait hendrerit iriure ipsum delenit, iriure, odio lobortis veniam, enim. Laoreet facilisi nulla volutpat consequat, qui vel facilisis duis eu veniam duis, facilisi dolor feugiat, aliquip, ad lobortis. Tation augue amet, ut consectetuer nibh nostrud sed commodo esse. Suscipit dolore praesent odio dolore, accumsan, iusto quis facilisis consequat ea eum duis.</p>
    </div>
  </main>

  <footer class="site-footer"><strong>Copyright</strong> | All rights reserved</footer>
</section>

</body>
</html>
```